Virtual Assistant/Online Marketing Business Card/Stationary

I need a professional but modern business card/stationary for my company in Dallas called Brivolo. Brivolo is a virtual assistant specializing in online marketing. I would like a unique design that stands out and makes my brand clear. Incorporating the logo is a must and have attached it to this brief.

Target Market(s)

small business owners & entrepreneurs, 35-65

Industry/Entity Type

Business

Contact Information for Business Card

Maren Tolk
marentolk@brivolo.biz
(555) 271-9064
brivolo.biz

Font styles to use
Sans Serif

Colors
f04a50
3176b5
9bcb3c

Requirements
Must have
• Colors that match the logo colors. Logo integration

```html
<!DOCTYPE html>
<html lang="en">
<head>
<meta charset="utf-8">
<title>Brivolo Business Card</title>
<link rel="stylesheet" href="https://fonts.googleapis.com/css2?family=Lato:wght@400;700;900&display=swap">
<style>
  :root {
    --red: #f04a50;
    --blue: #3176b5;
    --green: #9bcb3c;
    --ink: #1c1c1c;
    --grey: #555555;
    --paper: #ffffff;
    --backdrop: #e9e7e3;
  }
  * { box-sizing: border-box; margin: 0; padding: 0; }
  html, body {
    width: 1200px;
    height: 800px;
    overflow: hidden;
    background: var(--backdrop);
    font-family: "Lato", sans-serif;
  }
  .stage {
    width: 1200px;
    height: 800px;
    display: flex;
    align-items: center;
    justify-content: center;
    gap: 100px;
  }
  .card {
    position: relative;
    width: 360px;
    height: 600px;
    background: var(--paper);
    box-shadow: 0 4px 14px rgba(0,0,0,0.12);
  }
  .brand {
    display: flex;
    align-items: center;
    gap: 12px;
    color: var(--ink);
    font-weight: 900;
    letter-spacing: -1px;
    line-height: 1;
  }
  .brand-dot {
    border-radius: 50%;
    background: var(--red);
    flex: none;
  }
  .card-front .brand {
    position: absolute;
    left: 0; right: 0;
    top: 225px;
    justify-content: center;
    font-size: 66px;
  }
  .card-front .brand-dot { width: 30px; height: 30px; }
  .card-back .brand {
    position: absolute;
    left: 56px;
    top: 78px;
    font-size: 52px;
  }
  .card-back .brand-dot { width: 24px; height: 24px; }
  .identity {
    position: absolute;
    left: 150px;
    top: 212px;
  }
  .identity-name {
    font-size: 17px;
    font-weight: 700;
    color: var(--ink);
    text-transform: uppercase;
    letter-spacing: 0.3px;
  }
  .identity-role {
    font-size: 13px;
    color: var(--grey);
  }
  .contacts {
    position: absolute;
    left: 112px;
    top: 268px;
    list-style: none;
  }
  .contact {
    display: flex;
    align-items: center;
    gap: 10px;
    height: 36px;
    font-size: 14px;
    color: var(--ink);
  }
  .contact-icon {
    width: 26px;
    height: 26px;
    flex: none;
  }
  .accent-band {
    position: absolute;
    left: 0; right: 0;
    top: 500px;
    height: 16px;
    background: var(--red);
  }
</style>
</head>
<body>
<main class="stage">
  <section class="card card-front" aria-label="Card front">
    <div class="brand"><span class="brand-dot"></span>Brivolo</div>
  </section>

  <section class="card card-back" aria-label="Card back">
    <div class="brand"><span class="brand-dot"></span>Brivolo</div>

    <div class="identity">
      <div class="identity-name">Maren Tolk</div>
      <div class="identity-role">Creative Manager</div>
    </div>

    <ul class="contacts">
      <li class="contact">
        <svg class="contact-icon" viewBox="0 0 26 26" aria-hidden="true">
          <circle cx="13" cy="13" r="13" fill="var(--red)"/>
          <circle cx="13" cy="10" r="4" fill="#fff"/>
          <path d="M6 20c1.5-4 4-5 7-5s5.5 1 7 5z" fill="#fff"/>
        </svg>
        <span>Maren Tolk</span>
      </li>
      <li class="contact">
        <svg class="contact-icon" viewBox="0 0 26 26" aria-hidden="true">
          <circle cx="13" cy="13" r="13" fill="var(--red)"/>
          <rect x="6.5" y="8.5" width="13" height="9" fill="none" stroke="#fff" stroke-width="1.6"/>
          <path d="M6.5 8.5l6.5 5 6.5-5" fill="none" stroke="#fff" stroke-width="1.6"/>
        </svg>
        <span>marentolk@brivolo.biz</span>
      </li>
      <li class="contact">
        <svg class="contact-icon" viewBox="0 0 26 26" aria-hidden="true">
          <circle cx="13" cy="13" r="13" fill="var(--red)"/>
          <circle cx="13" cy="13" r="7.5" fill="none" stroke="#fff" stroke-width="1.6"/>
          <path d="M10 10.5c0 3 2.5 5.5 5.5 5.5l1-1.5-2-1-1 .8c-1-.5-1.8-1.3-2.3-2.3l.8-1-1-2z" fill="#fff"/>
        </svg>
        <span>(555) 271-9064</span>
      </li>
      <li class="contact">
        <svg class="contact-icon" viewBox="0 0 26 26" aria-hidden="true">
          <circle cx="13" cy="13" r="13" fill="var(--red)"/>
          <g fill="none" stroke="#fff" stroke-width="1.4">
            <circle cx="13" cy="13" r="7"/>
            <ellipse cx="13" cy="13" rx="3" ry="7"/>
            <path d="M6 13h14M7 9.5h12M7 16.5h12"/>
          </g>
        </svg>
        <span>brivolo.biz</span>
      </li>
    </ul>

    <div class="accent-band"></div>
  </section>
</main>
</body>
</html>
```